Custom Cakes- Nonprofit Organization Stationery Set

We are looking for a FULL set stationery design for our organization.
We create custom cakes for children in foster care and work with teens and young adults who have intellectual and developmental disabilities.
We spare no expense or amount of time creating fantastic cakes for these kids.... therefore are marketing materials need to reflect the same amount of fine details.

* Business Card Design (Front/Back preferred)
* Letterhead
* Envelope
* Presentation Folder

**** Tagline: Fostering Amazing Memories
would like this to appear on business card and marketing materials

Delia Marsh - Founder/Executive Director
www.marburycakes.org
info@marburycakes.org
1-844-TO-MARBRY
1-844-555-0172

Address is optional
PO Box 7316
Alpharetta, GA 30091

• Contact Information
• PO Box Address, design that will go well with textured/colored business card paper
• Updated: Business cards (maybe) textured paper, foiled, embossed or colored edges

```html
<!DOCTYPE html>
<html lang="en">
<head>
<meta charset="utf-8">
<title>Marbury Cakes Foundation – Presentation Folder</title>
<link href="https://fonts.googleapis.com/css2?family=Open+Sans:wght@400;600;700&family=Great+Vibes&display=swap" rel="stylesheet">
<style>
  :root {
    --backdrop: #d3d3d3;
    --folder-pink: #f3d0e1;
    --folder-pink-inner: #f1cadd;
    --pocket-blue: #c5e5f4;
    --pocket-blue-edge: #b3d8ea;
    --paper: #ffffff;
    --ink: #1f1f1f;
    --brand-pink: #e8268a;
    --brand-green: #6ad43a;
    --brand-blue: #1fa0dc;
  }
  * { margin: 0; padding: 0; box-sizing: border-box; }
  html, body { width: 1200px; height: 1000px; overflow: hidden; }
  body { background: var(--backdrop); font-family: "Open Sans", sans-serif; color: var(--ink); position: relative; }

  .folder-left { position: absolute; left: 166px; top: 178px; width: 454px; height: 639px; background: var(--folder-pink); }
  .folder-right { position: absolute; left: 620px; top: 182px; width: 420px; height: 635px; background: var(--folder-pink-inner); }

  .letterhead { position: absolute; left: 628px; top: 195px; width: 312px; height: 600px; background: var(--paper); overflow: hidden; }
  .letterhead-brand { position: absolute; left: 0; width: 100%; top: 78px; text-align: center; font-weight: 600; color: var(--ink); }
  .letterhead-brand .brand-name { font-size: 14px; display: block; line-height: 1.1; }
  .letterhead-brand .brand-sub { font-size: 7px; letter-spacing: 1px; display: block; }
  .letterhead-body { position: absolute; left: 55px; top: 146px; font-size: 8.6px; line-height: 11.6px; white-space: nowrap; }
  .letterhead-body h1 { font-size: 8.6px; font-weight: 700; margin-left: 65px; margin-bottom: 12px; }
  .letterhead-body p { text-indent: 5px; margin-bottom: 11.6px; }
  .letterhead-body p.tight { margin-bottom: 0; }
  .signature { position: absolute; left: 70px; top: 447px; font-family: "Great Vibes", cursive; font-size: 15px; }
  .signature-line { position: absolute; left: 70px; top: 468px; font-size: 5.5px; }

  .pocket { position: absolute; left: 0; top: 0; width: 1200px; height: 1000px; pointer-events: none; }

  .card-brand { font-family: "Open Sans", sans-serif; font-weight: 600; fill: var(--ink); }
</style>
</head>
<body>
  <div class="folder-left"></div>
  <div class="folder-right"></div>

  <div class="letterhead">
    <div class="letterhead-brand">
      <span class="brand-name">Marbury Cakes</span>
      <span class="brand-sub">FOUNDATION</span>
    </div>
    <div class="letterhead-body">
      <h1>Lorem ipsum dolor sit amet, ei eros vidit sonet eum</h1>
      <p class="tight">Lorem ipsum dolor sit amet, ei eros vidit sonet eum, sed ea aliquip</p>
      <p class="tight">labitur nec in, no solum ceteros est. Accumsan pertinacia an duo</p>
      <p class="tight">per habemus officiis, eos ex malis posidonium omittantur. At vero</p>
      <p>vis ei, an mea alia petentium dignissim, te justo omnium duo.</p>
      <p class="tight">Movet laoreet delicatissimi cum id. Essent dissentiet cu vix</p>
      <p>propriae ei sed. Euismod ornatus scaevola et pro.</p>
      <p class="tight">Verterem interesset disputationi vim et, laudem pertinax eu</p>
      <p class="tight">Ad scripta scaevola appetere usu, omnium forensibus ex pro</p>
      <p>mea ei. Eos ut ubique graeco insolens, etiam eleifend eu.</p>
      <p class="tight">In eos solum verterem facilisis, magna scaevola nec an.</p>
      <p class="tight">At dicam postea luptatum sea, sed te timeam mandamus</p>
      <p class="tight">tiam quo eu. Cetero concludaturque cu ius, ad sit</p>
      <p class="tight">bus. Eu sint nulla comprehensam qui. Dolore mei</p>
      <p>ruisset.</p>
      <p class="tight">Omnis intellegat intellegam duo cu, mel ex</p>
      <p class="tight">Verterem interesset disputationi vim et</p>
      <p class="tight">Ad scripta scaevola appetere usu, omnium</p>
      <p>mea ei. Eos ut ubique graeco insolens.</p>
      <p>Omnis intellegat intellegam duo cu.</p>
    </div>
    <div class="signature">Delia Marsh</div>
    <div class="signature-line">Delia Marsh, Founder/Executive Director</div>
  </div>

  <svg class="pocket" viewBox="0 0 1200 1000" xmlns="http://www.w3.org/2000/svg">
    <path d="M1040 182 L1005 182 Q950 185 930 240 L727 727 L620 727 L620 817 L1040 817 Z" fill="var(--pocket-blue)"/>
    <path d="M930 240 L727 727" stroke="var(--pocket-blue-edge)" stroke-width="1.5" fill="none"/>
    <path d="M620 727 L727 727 L735 817" stroke="var(--pocket-blue-edge)" stroke-width="1" fill="none"/>

    <g class="business-card">
      <rect x="822" y="657" width="92" height="103" fill="var(--brand-pink)" role="img" aria-label="Pink polka-dot pattern"/>
      <rect x="913" y="657" width="92" height="103" fill="var(--brand-green)" role="img" aria-label="Green and blue stripe pattern"/>
      <path d="M822 683 A12 25 0 0 1 822 733 Z" fill="var(--pocket-blue)"/>
      <path d="M1005 683 A12 25 0 0 0 1005 733 Z" fill="var(--pocket-blue)"/>
      <circle cx="913" cy="703" r="29" fill="var(--paper)"/>
      <text class="card-brand" x="913" y="703" font-size="7.5" text-anchor="middle">Marbury Cakes</text>
      <text class="card-brand" x="913" y="712" font-size="4" text-anchor="middle" letter-spacing="0.5">FOUNDATION</text>
    </g>
  </svg>
</body>
</html>
```